Website Design - Photo Shop Design - Functional Cash Register Layout for POS System

Design a webpage for Point of Sale site. A cash register page.

Page must have a good look. I have attached a file of a possible layout example - but need a much nicer design. I have also attached the site logo. which i will upload without background tomorrow hopefully.

Looking for a nice Fresh look , not dark and dingy.

Target Market(s)

Business

Industry/Entity Type

Business Software

Number of Pages Required

1 page

Colors
f59195
f04a50
ec1f27
fbd4d5
ffffff
f8f3f8
fdf0f6
feeeee
ecf5f6

Requirements
Must have
• Cash register layout for POS software site. Nice layout ,
Nice to have
• Try putting he register part on the left side as well as the right - invert the designs have them different to the layout example shown too.
Should not have
• Not to dark

```html
<!DOCTYPE html>
<html lang="en">
<head>
<meta charset="utf-8">
<title>TillNimbus – Cash Register</title>
<link href="https://fonts.googleapis.com/css2?family=Roboto:wght@300;400;500;700&display=swap" rel="stylesheet">
<style>
  :root {
    --pink-mid: #f59195;
    --red: #f04a50;
    --red-deep: #ec1f27;
    --pink-light: #fbd4d5;
    --white: #ffffff;
    --lilac-wash: #f8f3f8;
    --pink-wash: #fdf0f6;
    --blush: #feeeee;
    --ice: #ecf5f6;
    --ink: #222222;
    --ink-soft: #666666;
    --tile-border: #c4c4c4;
    --rule: #e4d3da;
  }
  * { box-sizing: border-box; margin: 0; padding: 0; }
  html, body { width: 1200px; height: 603px; overflow: hidden; background: var(--white); }
  body { font-family: "Roboto", Arial, sans-serif; position: relative; color: var(--ink); }

  .top-band { position: absolute; left: 0; top: 0; width: 1200px; height: 50px; background: var(--ice); }

  .sidebar { position: absolute; left: 0; top: 58px; width: 168px; height: 545px; background: var(--pink-wash); }
  .nav { list-style: none; position: absolute; left: 16px; top: 49px; width: 136px; }
  .nav-item {
    display: flex; align-items: center; gap: 6px; height: 36.6px; padding-left: 18px;
    color: var(--red); font-size: 8.5px; font-weight: 700; text-transform: uppercase; letter-spacing: 0;
    white-space: nowrap; border-bottom: 1px solid var(--rule);
  }
  .nav-item:last-child { border-bottom: none; }
  .nav-item svg { width: 11px; height: 11px; fill: var(--red); flex: none; }

  .brand { position: absolute; left: 188px; top: 66px; display: flex; align-items: center; gap: 6px; }
  .brand-dot { width: 18px; height: 18px; border-radius: 50%; background: var(--red-deep); }
  .brand-name { font-size: 22px; font-weight: 500; color: #333333; letter-spacing: -.5px; }

  .product-grid { position: absolute; left: 193px; top: 122px; display: grid; grid-template-columns: repeat(6, 96px); grid-auto-rows: 96px; column-gap: 12px; row-gap: 11px; }
  .product { border: 3px solid var(--tile-border); background: var(--white); display: flex; flex-direction: column; }
  .product-photo { height: 57px; margin: 2px 2px 0; background: linear-gradient(160deg, #d9d9d9 0%, #9a9a9a 55%, #5e5e5e 100%); }
  .product-name { padding: 6px 5px 0 5px; font-size: 10.5px; font-weight: 300; line-height: 1.2; color: var(--ink-soft); }
  .grid-rule { position: absolute; left: 186px; top: 432px; width: 427px; height: 1px; background: #bdbdbd; }

  .pager { position: absolute; left: 187px; top: 457px; width: 646px; display: flex; justify-content: space-between; font-size: 11.5px; color: var(--ink); }

  .category-bar { position: absolute; left: 187px; top: 480px; width: 646px; height: 38px; background: var(--pink-light); display: flex; align-items: center; }
  .category-bar svg { width: 14px; height: 20px; stroke: var(--red); stroke-width: 2; fill: none; }
  .cat-prev { margin: 0 6px 0 11px; }
  .cat-next { margin-left: auto; margin-right: 11px; }
  .category { height: 100%; display: flex; align-items: center; padding: 0 10px; font-size: 11.5px; font-weight: 700; letter-spacing: 1.6px; text-transform: uppercase; color: var(--red); border-right: 1px solid #f6c0c2; }
  .category:last-of-type { border-right: none; }

  .register-title { position: absolute; right: 27px; top: 61px; font-size: 13.5px; color: var(--ink); }
  .register { position: absolute; left: 851px; top: 82px; width: 321px; }
  .register-head { height: 38px; background: var(--pink-mid); display: flex; color: var(--white); }
  .customer { flex: 1; display: flex; align-items: center; gap: 5px; padding-left: 9px; font-size: 12px; }
  .customer svg { width: 15px; height: 16px; fill: var(--white); }
  .txn { width: 100px; border-left: 1px solid #f8b1b4; text-align: right; padding: 7px 12px 0 0; font-size: 11.5px; line-height: 1.15; }
  .register-body { height: 356px; background: var(--ice); position: relative; }
  .add-notes { position: absolute; left: 19px; top: 328px; transform: translateY(-40px); font-size: 11.5px; color: var(--red-deep); }
  .totals { position: absolute; left: 0; right: 0; top: 364px; transform: translateY(-37px); text-align: center; font-size: 8.3px; color: var(--ink); }

  .register-actions { position: absolute; left: 851px; top: 486px; width: 321px; height: 27px; display: flex; gap: 3px; }
  .btn-add { width: 26px; background: var(--blush); color: var(--red); font-size: 19px; font-weight: 300; display: flex; align-items: center; justify-content: center; }
  .btn-park { width: 135px; background: var(--blush); color: var(--red); font-size: 11.5px; display: flex; align-items: center; justify-content: center; }
  .btn-pay { flex: 1; margin-left: 3px; background: var(--pink-mid); color: var(--white); font-size: 11.5px; font-weight: 700; display: flex; align-items: center; justify-content: space-between; padding: 0 12px 0 28px; }

  .register-foot { position: absolute; left: 851px; top: 520px; width: 321px; height: 77px; background: var(--ice); }
</style>
</head>
<body>
  <div class="top-band"></div>

  <aside class="sidebar">
    <ul class="nav">
      <li class="nav-item"><svg viewBox="0 0 12 12"><path d="M6 1 0.5 6h1.6v5h3V8h1.8v3h3V6h1.6z"/></svg>Enter Sale</li>
      <li class="nav-item"><svg viewBox="0 0 12 12"><path d="M5 1h2v4.5h2L6 9 3 5.5h2zM1 8h1.5v2h7V8H11v3.5H1z"/></svg>Parked / Layby Orders</li>
      <li class="nav-item"><svg viewBox="0 0 12 12"><path d="M1.5 1h1.2v10.5H1.5zM3 1.5h8l-2 3 2 3H3z"/></svg>Completed Sales</li>
      <li class="nav-item"><svg viewBox="0 0 12 12"><path d="M1 2h10v9.5H1zm1.2 3v5.3h7.6V5zM3 .5h1.2V3H3zm4.8 0H9V3H7.8z"/></svg>Appointments</li>
      <li class="nav-item"><svg viewBox="0 0 12 12"><circle cx="6" cy="3.3" r="2.6"/><path d="M1 11.5c0-3 2.2-5 5-5s5 2 5 5z"/></svg>Back Office</li>
      <li class="nav-item"><svg viewBox="0 0 12 12"><path d="M10.5 1v4H6.5l1.6-1.6A3.2 3.2 0 0 0 2.9 5H1.2a4.8 4.8 0 0 1 8-2.7zM1.5 11V7h4L3.9 8.6A3.2 3.2 0 0 0 9.1 7h1.7a4.8 4.8 0 0 1-8 2.7z"/></svg>Refresh Data</li>
    </ul>
  </aside>

  <div class="brand"><span class="brand-dot"></span><span class="brand-name">TillNimbus</span></div>

  <main class="product-grid">
    <div class="product"><div class="product-photo" role="img" aria-label="Photo of a fish taco"></div><div class="product-name">Fish Taco</div></div>
    <div class="product"><div class="product-photo" role="img" aria-label="Photo of a scotch fillet steak"></div><div class="product-name">250g Scotch Fillet</div></div>
    <div class="product"><div class="product-photo" role="img" aria-label="Photo of seafood chowder"></div><div class="product-name">Seafood Chowder</div></div>
    <div class="product"><div class="product-photo" role="img" aria-label="Photo of a scoop of ice cream"></div><div class="product-name">Kids Scoop Icecream</div></div>
    <div class="product"><div class="product-photo" role="img" aria-label="Photo of buffalo wings"></div><div class="product-name">Buffalo Wings</div></div>
    <div class="product"><div class="product-photo" role="img" aria-label="Photo of a steak"></div><div class="product-name">New York Cut Steak</div></div>

    <div class="product"><div class="product-photo" role="img" aria-label="Photo of a fish dish"></div><div class="product-name">Fish of the day</div></div>
    <div class="product"><div class="product-photo" role="img" aria-label="Photo of a burger"></div><div class="product-name">Roadster Burger</div></div>
    <div class="product"><div class="product-photo" role="img" aria-label="Photo of mini burgers"></div><div class="product-name">Mini Burgers</div></div>
    <div class="product"><div class="product-photo" role="img" aria-label="Photo of ice cream and sorbet"></div><div class="product-name">Ice Cream &amp; Sorbet</div></div>
    <div class="product"><div class="product-photo" role="img" aria-label="Photo of a burger"></div><div class="product-name">Gaucho Burger</div></div>
    <div class="product"><div class="product-photo" role="img" aria-label="Photo of nachos with guacamole"></div><div class="product-name">Guacamole &amp; Nachos</div></div>

    <div class="product"><div class="product-photo" role="img" aria-label="Photo of buffalo wings"></div><div class="product-name">Buffalo Wings</div></div>
    <div class="product"><div class="product-photo" role="img" aria-label="Photo of a steak"></div><div class="product-name">New York Cut Steak</div></div>
    <div class="product"><div class="product-photo" role="img" aria-label="Photo of apple pie"></div><div class="product-name">Apple Pie</div></div>
    <div class="product"><div class="product-photo" role="img" aria-label="Photo of a bowl of soup"></div><div class="product-name">Soup of the Day</div></div>
    <div class="product"><div class="product-photo" role="img" aria-label="Photo of fried chicken"></div><div class="product-name">Deep Fried Chicken</div></div>
    <div class="product"><div class="product-photo" role="img" aria-label="Photo of a burger"></div><div class="product-name">Garage Burger</div></div>
  </main>
  <div class="grid-rule"></div>

  <nav class="pager"><span>Prev</span><span>Next</span></nav>

  <nav class="category-bar">
    <svg class="cat-prev" viewBox="0 0 14 20"><path d="M11 2 3 10l8 8"/></svg>
    <span class="category">List</span>
    <span class="category">All</span>
    <span class="category">Deats</span>
    <span class="category">Uncategorized</span>
    <svg class="cat-next" viewBox="0 0 14 20"><path d="M3 2l8 8-8 8"/></svg>
  </nav>

  <div class="register-title">My Shop/Cash Register 1</div>

  <section class="register">
    <header class="register-head">
      <div class="customer"><svg viewBox="0 0 15 16"><circle cx="7.5" cy="4.3" r="4"/><path d="M0 16c0-4.5 3.3-7 7.5-7S15 11.5 15 16z"/></svg>Select Customer</div>
      <div class="txn">Transaction#<br>00016</div>
    </header>
    <div class="register-body">
      <span class="add-notes">Add Nates</span>
      <p class="totals">Subtotal: $0.00 | Tax: $0.00 | Disc: | Total: $0.00 Paid: $0.00</p>
    </div>
  </section>

  <div class="register-actions">
    <div class="btn-add">+</div>
    <div class="btn-park">SAVE &amp; PARK / LAYBY</div>
    <div class="btn-pay"><span>PAY</span><span>$ 0.00</span></div>
  </div>

  <div class="register-foot"></div>
</body>
</html>
```